WEB DESIGN AGENCY WEBSITE

the website is for "Web design and development company" VORELIX LTD.

I need a very clean, simple, professional design, it will be an ambassador for the company

1- I want one page design that begins with full screen image slider (4 images)
ex. (https://quandrelworks.com/)
2- images representation is the most important thing, so i need a 3 images sliders to be created that represents the below:
a. 1st image represents the company (WEB DESIGNING)
b. 2nd image represents (FULLY RESPONSIVE WEBSITES)
c. 3rd image represents (ECOMMERCE WEBSITES)
D. Social media integration
Please find the pictures I bought attached. Will send you the original files once the design is approved ( PLEASE FEEL FREE TO USE ANY OTHER PICS IF YOU FIND IT MORE CREATIVE )

it is very important that the 4 images have the same theme, very creative and presentable

3- the website must be responsive, and the mobile view is very very important, as more than 60% of web users access websites by phone or tablets (check quandrelworks website by phone)

4- the rest of the page will have the contents, please be creative this is a webdesign agency, need something WOW and professional and clean

website i like for the rest of the page:
https://www.haldimore.com/stylo
( i like the design, how the images are created, the colors, dark grey color in background everything)

again please make sure that all pictures used have excellent quality, creative and presentable, have the same theme

all information needed, about the contents you will find in this link:
http://vorelixltd.co.uk/VORELIXWEBSITE/HTML/index.html

please don't use any of the graphics elements, or the deign (we don't like it) it is just a template to display contents

you can change the logo color to white, if that will serve the design better, but of course it is much better to keep the logo color to keep the company identity

5- i need a contact us form at the end of the page

6- please create a portfolio part

many thanks for your time and efforts and good luck, please impress me :) whoever is the winner, will always have business with us

i have attached the logo and logo font

Requirements
Nice to have
• Dark grey back ground
Should not have
• no people pictures please
• i need specially made images like https://www.haldimore.com/stylo having same theme , look and feel, customized pics

```html
<!DOCTYPE html>
<html lang="en">
<head>
<meta charset="utf-8">
<title>VORELIX LTD — Web Design &amp; Development</title>
<link href="https://fonts.googleapis.com/css2?family=Raleway:wght@300;400;500;600&family=Open+Sans:wght@400;600&display=swap" rel="stylesheet">
<style>
:root{
  --accent:#1b9ad6;
  --orange:#e0692a;
  --dark:#2b2827;
  --darker:#1f1d1c;
  --light:#ffffff;
  --grey-band:#e4e4e4;
  --text:#555555;
  --muted:#b9b5b2;
}
*{margin:0;padding:0;box-sizing:border-box}
html,body{width:1200px;height:5217px;overflow:hidden}
body{font-family:"Open Sans",Arial,sans-serif;color:var(--text);background:var(--light);position:relative}
.section{position:absolute;left:0;width:1200px}
.section-title{font-family:"Raleway",Arial,sans-serif;font-weight:400;font-size:40px;letter-spacing:1px;text-align:center;color:var(--accent)}
.section-title.on-dark{color:var(--light)}
.lead{font-size:15px;line-height:23px;text-align:center}

/* hero */
.hero{top:0;height:515px}
.hero-photo{position:absolute;inset:0;background:
  radial-gradient(ellipse 38% 55% at 42% 45%,rgba(70,78,88,.95) 0%,rgba(70,78,88,.6) 55%,rgba(70,78,88,0) 100%),
  radial-gradient(ellipse 30% 40% at 85% 70%,rgba(236,232,224,.95) 0%,rgba(236,232,224,0) 100%),
  linear-gradient(100deg,#6d533f 0%,#8a6a50 30%,#7b6352 55%,#a79583 80%,#d2c8bb 100%)}
.hero-shade{position:absolute;left:0;top:0;width:100%;height:130px;background:linear-gradient(180deg,rgba(0,0,0,.55),rgba(0,0,0,0))}
.nav{position:absolute;left:0;top:0;width:100%;height:120px}
.brand{position:absolute;left:175px;top:38px;display:flex;align-items:center;gap:10px}
.brand-mark{width:30px;height:30px;background:var(--light)}
.brand-name{font-family:"Raleway",Arial,sans-serif;font-weight:600;font-size:18px;letter-spacing:2px;color:var(--light)}
.nav-links{position:absolute;left:520px;top:56px;display:flex;gap:28px;list-style:none}
.nav-links li{font-family:"Raleway",Arial,sans-serif;font-size:13px;font-weight:500;color:var(--light);letter-spacing:.5px}
.nav-links li.active{color:var(--accent)}
.nav-social{position:absolute;left:900px;top:26px;display:flex;gap:6px}
.nav-social span{width:14px;height:14px;border-radius:50%;background:var(--accent)}

/* creative */
.creative{top:515px;height:580px;background:var(--light)}
.creative .section-title{position:absolute;top:60px;width:100%}
.creative .lead{position:absolute;top:125px;left:310px;width:580px}
.creative-art{position:absolute;left:310px;top:295px;width:580px;height:250px;background:
  radial-gradient(ellipse 22% 40% at 50% 45%,rgba(43,183,214,.55) 0%,rgba(43,183,214,0) 100%),
  radial-gradient(ellipse 16% 30% at 18% 55%,rgba(217,71,58,.35) 0%,rgba(217,71,58,0) 100%),
  radial-gradient(ellipse 18% 30% at 84% 60%,rgba(242,181,60,.35) 0%,rgba(242,181,60,0) 100%),
  radial-gradient(ellipse at 50% 95%,#d8d8d8 0%,#f4f4f4 45%,#ffffff 70%)}

/* services */
.services{top:1095px;height:1445px;background:var(--dark)}
.services .section-title{position:absolute;top:60px;width:100%}
.timeline{position:absolute;left:608px;top:140px;width:3px;height:1220px;background:var(--orange)}
.service{position:absolute;left:0;width:1200px;height:140px}
.service-name{position:absolute;left:330px;width:190px;top:32px;text-align:right;font-family:"Raleway",Arial,sans-serif;font-weight:600;font-size:15px;line-height:22px;color:var(--light);letter-spacing:.5px}
.service-icon{position:absolute;left:571px;top:26px;width:78px;height:78px;border-radius:50%;background:var(--orange);display:flex;align-items:center;justify-content:center}
.service-head{position:absolute;left:680px;top:26px;width:360px;font-family:"Raleway",Arial,sans-serif;font-size:15px;line-height:20px;color:var(--light);letter-spacing:.5px}
.service-text{position:absolute;left:680px;top:72px;width:360px;font-size:12px;line-height:17px;color:var(--muted)}

/* portfolio */
.portfolio-head{top:2540px;height:173px;background:var(--light)}
.portfolio-head .section-title{position:absolute;top:66px;width:100%}
.portfolio{top:2713px;height:567px}
.tile{position:absolute}
.tile-web{left:0;top:0;width:598px;height:567px;background:
  radial-gradient(ellipse 34% 26% at 50% 55%,rgba(12,12,12,.9) 0%,rgba(12,12,12,0) 100%),
  radial-gradient(ellipse at 35% 55%,#3a3a3a 0%,#262626 55%,#1c1c1c 100%)}
.tile-caption{position:absolute;left:210px;top:238px;width:230px}
.tile-caption h3{font-family:"Raleway",Arial,sans-serif;font-size:15px;font-weight:600;color:var(--light);letter-spacing:.5px}
.tile-caption p{font-size:11px;line-height:15px;color:#bbb;margin-top:6px}
.tile-app{left:598px;top:0;width:301px;height:278px;background:
  radial-gradient(ellipse 45% 40% at 55% 45%,rgba(240,242,246,.95) 0%,rgba(240,242,246,0) 100%),
  linear-gradient(135deg,#6c574e,#8a7266)}
.tile-tablet{left:899px;top:0;width:301px;height:278px;background:
  radial-gradient(ellipse 28% 38% at 45% 48%,rgba(53,169,200,.9) 0%,rgba(53,169,200,0) 100%),
  linear-gradient(135deg,#efefef,#d4d6d8)}
.tile-phones{left:598px;top:278px;width:602px;height:289px;background:
  radial-gradient(ellipse 35% 30% at 50% 55%,rgba(232,236,240,.75) 0%,rgba(232,236,240,0) 100%),
  linear-gradient(135deg,#7289a6,#5f7898 50%,#4e6686)}
.dot-marker{position:absolute;left:292px;top:530px;width:8px;height:8px;border-radius:50%;background:var(--light)}

/* team */
.team{top:3280px;height:504px;background:var(--grey-band)}
.team .section-title{position:absolute;top:70px;width:100%}
.team .lead{position:absolute;top:130px;left:330px;width:540px;color:#777}
.team-photo{position:absolute;left:260px;top:225px;width:660px;height:279px;background:
  radial-gradient(ellipse 40% 30% at 50% 30%,rgba(214,174,140,.8) 0%,rgba(214,174,140,0) 100%),
  linear-gradient(180deg,#e4e4e4 0%,#d0bba6 40%,#6e86a6 85%,#56719a 100%)}

/* process */
.process{top:3784px;height:476px;background:var(--dark)}
.process .section-title{position:absolute;top:68px;width:100%}
.process .lead{position:absolute;top:130px;left:300px;width:600px;color:var(--muted)}
.step{position:absolute;top:226px;width:132px;text-align:center}
.step-circle{width:132px;height:132px;border-radius:50%;border:2px solid var(--light);display:flex;align-items:center;justify-content:center}
.step-label{margin-top:20px;font-family:"Raleway",Arial,sans-serif;font-size:16px;color:var(--light)}
.step-arrow{position:absolute;top:286px;width:52px;height:12px}

/* testimonials */
.testimonials{top:4260px;height:533px;background:var(--light)}
.testimonials .section-title{position:absolute;top:70px;width:100%}
.quote{position:absolute;top:130px;left:300px;width:600px;font-size:14px;line-height:21px;text-align:center;color:#666}
.arrow-nav{position:absolute;top:195px;width:26px;height:20px}
.author-icon{position:absolute;left:586px;top:222px;width:28px;height:28px}
.author{position:absolute;top:258px;width:100%;text-align:center;font-size:14px;font-weight:600;color:#444}
.hands{position:absolute;left:0;top:296px;width:1200px;height:237px;background:
  linear-gradient(180deg,#ffffff 0%,rgba(255,255,255,0) 35%),
  linear-gradient(90deg,#e2b595 0%,#c98f6c 20%,#edc6a8 40%,#b97d5c 60%,#e4b898 80%,#c48a68 100%);}
.hands::after{content:"";position:absolute;left:0;bottom:0;width:100%;height:70px;background:linear-gradient(180deg,rgba(40,32,30,0),#2e2624)}

/* contact */
.contact{top:4793px;height:424px;background:var(--darker)}
.contact-info{position:absolute;left:205px;top:70px;width:360px}
.contact-info h2{font-family:"Raleway",Arial,sans-serif;font-weight:400;font-size:22px;color:var(--accent);letter-spacing:1px}
.contact-mark{width:34px;height:34px;background:var(--accent);margin-top:22px}
.contact-info dl{margin-top:18px;font-size:12px;line-height:17px;color:#cfcfcf}
.contact-info dt{color:#fff;margin-top:10px}
.contact-social{display:flex;gap:6px;margin-top:16px}
.contact-social span{width:14px;height:14px;border-radius:50%;background:#777}
.copyright{font-size:11px;color:#888;margin-top:10px}
.map{position:absolute;left:609px;top:0;width:591px;height:424px;background:linear-gradient(135deg,#ecebe6 0%,#e2e0d8 40%,#d6d9dd 70%,#ecebe6 100%)}
</style>
</head>
<body>

<header class="section hero">
  <div class="hero-photo" role="img" aria-label="Photo of hands holding a tablet showing a web design layout on a wooden desk with glasses and a notebook"></div>
  <div class="hero-shade"></div>
  <nav class="nav">
    <div class="brand"><span class="brand-mark"></span><span class="brand-name">VORELIX</span></div>
    <ul class="nav-links">
      <li class="active">ABOUT US</li><li>SERVICES</li><li>PORTFOLIO</li><li>TEAM</li><li>TESTIMONIAL</li><li>CONTACT US</li>
    </ul>
    <div class="nav-social"><span></span><span></span><span></span><span></span></div>
  </nav>
</header>

<section class="section creative">
  <h2 class="section-title">WE ARE CREATIVE</h2>
  <p class="lead">We are a creative web design agency. Our design experts offer the best balance of creativeness and user experience with their result oriented innovation and you get more than just a nice-looking design. We add value to your business and assist you in presenting a professional front to the marketplace through objective driven digital solutions by providing original creative designs to all types of businesses, small to corporate level.</p>
  <div class="creative-art" role="img" aria-label="Illustration of a desktop computer surrounded by design tools, pencils, a camera and a plant"></div>
</section>

<section class="section services">
  <h2 class="section-title on-dark">OUR SERVICES</h2>
  <div class="timeline"></div>

  <article class="service" style="top:250px">
    <h3 class="service-name">WEB DESIGN AND<br>DEVELOPMENT</h3>
    <div class="service-icon"><svg width="34" height="30" viewBox="0 0 34 30"><rect x="2" y="3" width="30" height="19" fill="none" stroke="#fff" stroke-width="2"/><path d="M12 28h10M17 22v6" stroke="#fff" stroke-width="2"/></svg></div>
    <p class="service-head">WE ARE CREATIVE AND HIGHLY<br>EXPERIENCED DEVELOPERS</p>
    <p class="service-text">Unbelievably affordable web design packages for small, medium and large businesses. We ensure you get a visually striking and functional website.</p>
  </article>

  <article class="service" style="top:452px">
    <h3 class="service-name">ECOMMERCE<br>DEVELOPMENT</h3>
    <div class="service-icon"><svg width="34" height="30" viewBox="0 0 34 30"><path d="M2 4h6l4 15h16l3-11H10" fill="none" stroke="#fff" stroke-width="2"/><circle cx="14" cy="25" r="2.5" fill="#fff"/><circle cx="26" cy="25" r="2.5" fill="#fff"/></svg></div>
    <p class="service-head">GENERATE MORE SALES</p>
    <p class="service-text">Our ecommerce designs are built to impress visitors and turn them into buyers, with smooth checkout paths, better conversions and higher profits for clients.</p>
  </article>

  <article class="service" style="top:660px">
    <h3 class="service-name">CMS<br>DEVELOPMENT</h3>
    <div class="service-icon"><svg width="32" height="32" viewBox="0 0 32 32"><rect x="3" y="5" width="24" height="24" fill="none" stroke="#fff" stroke-width="2"/><path d="M10 20l12-12 3 3-12 12h-3z" fill="#fff"/></svg></div>
    <p class="service-head">CONTENT MANAGEMENT SYSTEM</p>
    <p class="service-text">CMS makes it easy for our clients to manage their websites without programming skills, keeping every page up to date.</p>
  </article>

  <article class="service" style="top:869px">
    <h3 class="service-name">ONLINE<br>MARKETING</h3>
    <div class="service-icon"><svg width="32" height="30" viewBox="0 0 32 30"><path d="M3 27h26" stroke="#fff" stroke-width="2"/><rect x="5" y="18" width="5" height="8" fill="#fff"/><rect x="13" y="12" width="5" height="14" fill="#fff"/><rect x="21" y="5" width="5" height="21" fill="#fff"/></svg></div>
    <p class="service-head">SEO &amp; SEM SERVICES</p>
    <p class="service-text">Get qualified leads and rank high on search engines with our careful search engine optimisation and paid campaign services.</p>
  </article>

  <article class="service" style="top:1078px">
    <h3 class="service-name">SOCIAL MEDIA<br>INTEGRATION</h3>
    <div class="service-icon"><svg width="32" height="30" viewBox="0 0 32 30"><path d="M4 4h24v16H14l-7 6v-6H4z" fill="none" stroke="#fff" stroke-width="2"/></svg></div>
    <p class="service-head">MAKE YOUR BRAND SOCIALLY RELEVANT</p>
    <p class="service-text">We connect your brand to a powerful social following with creative and specially tailored social media campaigns for your brand.</p>
  </article>

  <article class="service" style="top:1293px">
    <h3 class="service-name">MAINTENANCE</h3>
    <div class="service-icon"><svg width="32" height="32" viewBox="0 0 32 32"><path d="M6 6l20 20M26 6L6 26" stroke="#fff" stroke-width="3"/></svg></div>
    <p class="service-head">FREE SUPPORT</p>
    <p class="service-text">We believe in building long-term relationships with our clients, and that is why we offer free website maintenance after project delivery.</p>
  </article>
</section>

<section class="section portfolio-head">
  <h2 class="section-title">OUR PORTFOLIO</h2>
</section>

<section class="section portfolio">
  <div class="tile tile-web" role="img" aria-label="Desktop, laptop, tablet and phone showing a responsive website on a dark background">
    <div class="tile-caption"><h3>WEBSITE DESIGN</h3><p>Responsive layouts crafted for every screen and device size.</p></div>
    <span class="dot-marker"></span>
  </div>
  <div class="tile tile-app" role="img" aria-label="Tablet showing an app dashboard on a brown background"></div>
  <div class="tile tile-tablet" role="img" aria-label="Tablet with a turquoise cover on a light surface"></div>
  <div class="tile tile-phones" role="img" aria-label="Two smartphones showing a mobile app on a blue background"></div>
</section>

<section class="section team">
  <h2 class="section-title">OUR TEAM</h2>
  <p class="lead">Lorem Ipsum is simply dummy text of the printing and typesetting industry. Lorem Ipsum has been the industry's standard dummy text ever since the 1500s, when an unknown printer took a galley of type.</p>
  <div class="team-photo" role="img" aria-label="Photo of the team gathered around a laptop"></div>
</section>

<section class="section process">
  <h2 class="section-title on-dark">WORK PROCESS</h2>
  <p class="lead">As a web design development company we build websites that perfectly captures owner's imagination without compromising usability, marketability and functionality.</p>

  <div class="step" style="left:212px">
    <div class="step-circle"><svg width="44" height="54" viewBox="0 0 44 54"><path d="M22 6a14 14 0 0 0-8 25v8h16v-8a14 14 0 0 0-8-25zM15 45h14M17 50h10" fill="none" stroke="#fff" stroke-width="2"/></svg></div>
    <div class="step-label">An Idea</div>
  </div>
  <svg class="step-arrow" style="left:360px" viewBox="0 0 52 12"><path d="M0 6h44M40 1l6 5-6 5" fill="none" stroke="var(--accent)" stroke-width="2" stroke-dasharray="4 3"/></svg>

  <div class="step" style="left:431px">
    <div class="step-circle"><svg width="54" height="54" viewBox="0 0 54 54"><path d="M8 8l38 38M46 8L8 46" stroke="#fff" stroke-width="3"/></svg></div>
    <div class="step-label">Designing</div>
  </div>
  <svg class="step-arrow" style="left:579px" viewBox="0 0 52 12"><path d="M0 6h44M40 1l6 5-6 5" fill="none" stroke="var(--accent)" stroke-width="2" stroke-dasharray="4 3"/></svg>

  <div class="step" style="left:647px">
    <div class="step-circle"><svg width="60" height="48" viewBox="0 0 60 48"><rect x="3" y="3" width="54" height="42" fill="none" stroke="#fff" stroke-width="2"/><path d="M3 12h54M22 22l-7 7 7 7M38 22l7 7-7 7M33 20l-6 18" fill="none" stroke="#fff" stroke-width="2"/></svg></div>
    <div class="step-label">Development</div>
  </div>
  <svg class="step-arrow" style="left:795px" viewBox="0 0 52 12"><path d="M0 6h44M40 1l6 5-6 5" fill="none" stroke="var(--accent)" stroke-width="2" stroke-dasharray="4 3"/></svg>

  <div class="step" style="left:866px">
    <div class="step-circle"><svg width="50" height="56" viewBox="0 0 50 56"><path d="M25 3c9 8 11 20 7 32H18C14 23 16 11 25 3zM18 35l-8 10h8M32 35l8 10h-8M25 40v12" fill="none" stroke="#fff" stroke-width="2"/><circle cx="25" cy="20" r="4" fill="#fff"/></svg></div>
    <div class="step-label">Launch</div>
  </div>
</section>

<section class="section testimonials">
  <h2 class="section-title">OUR TESTIMONIALS</h2>
  <p class="quote">"Many desktop publishing packages and web page editors now use Lorem Ipsum as their default model text, and a search for 'lorem ipsum' will uncover many web sites still in their infancy. Various versions have evolved over the years"</p>
  <svg class="arrow-nav" style="left:140px" viewBox="0 0 26 20"><path d="M10 2L2 10l8 8M2 10h22" fill="none" stroke="#999" stroke-width="2.5"/></svg>
  <svg class="arrow-nav" style="left:1034px" viewBox="0 0 26 20"><path d="M16 2l8 8-8 8M24 10H2" fill="none" stroke="var(--accent)" stroke-width="2.5"/></svg>
  <svg class="author-icon" viewBox="0 0 28 28"><circle cx="14" cy="14" r="12" fill="none" stroke="var(--accent)" stroke-width="2"/><circle cx="14" cy="11" r="4" fill="var(--accent)"/><path d="M7 22c2-5 12-5 14 0" fill="var(--accent)"/></svg>
  <p class="author">Rowan Pell</p>
  <div class="hands" role="img" aria-label="Photo of many raised hands giving thumbs up"></div>
</section>

<footer class="section contact">
  <div class="contact-info">
    <h2>CONTACT US</h2>
    <div class="contact-mark"></div>
    <dl>
      <dt>Location</dt>
      <dd>Kelvane Court, 7 Tallis Yard<br>Ashbridge AB4 2QT, United Kingdom</dd>
      <dt>Call us</dt>
      <dd>+44 20 7946 0318</dd>
      <dt>Email</dt>
      <dd>hello@vorelixltd.co.uk</dd>
    </dl>
    <div class="contact-social"><span></span><span></span><span></span><span></span></div>
    <p class="copyright">© VORELIX LTD 2017</p>
  </div>
  <div class="map" role="img" aria-label="Street map showing the office location with a red pin"></div>
</footer>

</body>
</html>
```